wine label design

i'm a fine wine store based in new zealand which buys quality bulk wine and bottles it, passing on the significant savings onto the customer. i require a brand name and design which is cool/ sharp and contempory. the wines will be all still wines, there won't be any sparkling wines under this brand. i've used brand names like harbourlight wine company for previous designs/label but want something more edgier. we thought about a brand name 'sky above the vines' or 'harbourlight wine co' but couldn't get a design to match the title of brand, if you have any thoughts on this send thru your design. take into account color they have to be bold as i am printing these thru a digital printer. the label is a wrap around design, the dimensions are approximately 80 or 90 mm high and 210 mm wide. have a look at these links, i think they have some x-factor to them: http://www.marlowvale.example/store/product_images/p/855/velora__34476_zoom.jpg: OR

http://static3.cellarfinder.example/images/labels/35/24/ember-in-the-fog-shiraz-petite-sirah-south-australia-10203524.jpg: OR

http://www.bottlebarn.example/ui/productimages/25223/25223_w240.jpg: OR

http://www.vintrail.example/images/viewWinery.php?pic=238291

Take into account i have to be able put a wine desription on the back label, barcode and a few technical details required by law. on the front label all i require is space to put the grape variety, area and vintage. i need the grape type to really stand out.
Updates

Reason: hi, the designs coming thru look good, just need a little more changes, also please read thru the brief, there are a few things i have noted such as label size etc etc

Target Market(s)

am after a label the cool/edgy/contempoary that appeals to the educated well off customer that willing to give something new a go by the look of the label that is cool and edgy.

Industry/Entity Type

Boutique

Requirements
Must have
• bold bold bold, it must stand out on the shelf
Nice to have
• a title/brand name that links what i'm doing, from what i'm doing the name 'harbourlight wine co' is probably best suited.
Should not have
• basic boring artwork and small text, the bigger the text the better

```html
<!DOCTYPE html>
<html lang="en">
<head>
<meta charset="utf-8">
<title>Sky Above The Vines – Merlot Label</title>
<link href="https://fonts.googleapis.com/css2?family=Federo&display=swap" rel="stylesheet">
<style>
  :root {
    --ink: #0c0c0c;
    --paper: #ffffff;
    --panel: #050505;
    --panel-sheen: #2a2a2a;
  }
  html, body {
    margin: 0;
    padding: 0;
    overflow: hidden;
    background: var(--paper);
  }
  .label {
    position: relative;
    width: 1200px;
    height: 457px;
    background: var(--paper);
    color: var(--ink);
    font-family: "Federo", sans-serif;
    overflow: hidden;
  }
  .brand-panel {
    position: absolute;
    left: 490px;
    top: 25px;
    width: 226px;
    height: 275px;
  }
  .brand-panel__name {
    position: absolute;
    inset: 0;
    display: flex;
    flex-direction: column;
    align-items: center;
    justify-content: center;
    gap: 6px;
    color: var(--paper);
    font-size: 30px;
    line-height: 1;
    text-transform: uppercase;
    letter-spacing: 2px;
    text-align: center;
  }
  .label__text {
    position: absolute;
    left: 0;
    width: 100%;
    margin: 0;
    text-align: center;
    font-weight: 400;
    line-height: 1;
  }
  .variety {
    top: 311px;
    font-size: 25px;
    font-variant: small-caps;
    text-transform: capitalize;
    left: -3px;
  }
  .brand-name {
    top: 348px;
    font-size: 35px;
    text-transform: uppercase;
    letter-spacing: 0.5px;
  }
  .vintage {
    top: 395px;
    font-size: 20px;
    left: -3px;
  }
  .region {
    top: 425px;
    font-size: 10px;
    font-variant: small-caps;
    left: -3px;
  }
</style>
</head>
<body>
  <main class="label">
    <div class="brand-panel">
      <svg width="226" height="275" viewBox="0 0 226 275" aria-hidden="true">
        <defs>
          <linearGradient id="panel-sheen" x1="0" y1="0" x2="1" y2="1">
            <stop offset="0" stop-color="var(--panel-sheen)"/>
            <stop offset="0.45" stop-color="var(--panel)"/>
            <stop offset="1" stop-color="var(--panel)"/>
          </linearGradient>
        </defs>
        <rect x="2" y="2" width="222" height="271" fill="none" stroke="var(--ink)" stroke-width="4"/>
        <rect x="10" y="10" width="206" height="255" fill="url(#panel-sheen)"/>
      </svg>
      <div class="brand-panel__name">
        <span>Sky</span>
        <span>Above</span>
        <span>The Vines</span>
      </div>
    </div>

    <h2 class="label__text variety">Merlot</h2>
    <h1 class="label__text brand-name">Sky Above The Vines</h1>
    <p class="label__text vintage">2007</p>
    <p class="label__text region">Region</p>
  </main>
</body>
</html>
```